Meadowbrook Fellowship Chapel Banner Design

Designing 6 banners (3 + 3 that will hang on opposite sides of our auditorium) that are 10 feet long by 4 feet wide.

Use our branding guide - specifically item 4 (vertical logo) and item 5 (icon logo).

Design elements found in our AWAKE booklet, we would like to see designs that utilize the white, green and blue colour palettes but NOT the grey. Other colours may be incorporated (e.g. coral).

We are looking for 3 banner designs that would match on either side of the auditorium, the first banner incorporating the word "TRUTH", the second incorporating the word "LOVE", and the third incorporating the word "MISSION".

We interested in incorporating graphics such as trees or outdoor themes.

Font styles to use
Other font styles liked:
• Montserrat

Colors
34a7d7
00a990
f47c35

Requirements
Must have
• Banner Type #1 include the word "TRUTH"
Banner Type #2 include the word "LOVE"
Banner Type #3 include the word "MISSION"

Colour scheme must include CMYK 54 / 5 / 16 / 0 (which is available in the branding guide.) We have selected the three colours, included below in the brief.

From the branding guide - utilize #5 (icon) for the banner.

UPDATE: After reviewing the initial submissions, we are asking for designs that ONLY incorporate #5 - the ICON logo for the banners.
Nice to have
• It would be nice to have some creativity with the colour ... though a more minimalistic style is preferred.

Graphic adaptations such as trees in the background would be of interest.
Should not have
• Colour scheme should not be gray scale.

The banners should NOT be too busy.

Scripture verses (written out) are not necessary.

```html
<!DOCTYPE html>
<html lang="en">
<head>
<meta charset="utf-8">
<title>Meadowbrook Fellowship Chapel — Auditorium Banners</title>
<link href="https://fonts.googleapis.com/css2?family=Bebas+Neue&family=Montserrat:wght@700&display=swap" rel="stylesheet">
<style>
  :root {
    --page: #ffffff;
    --white: #ffffff;
    --blue-deep: #1a74a6;
    --blue-mid: #2590c4;
    --blue-bright: #34a7d7;
    --cyan-light: #5fd2ee;
  }
  html, body {
    margin: 0;
    padding: 0;
    width: 1200px;
    height: 911px;
    overflow: hidden;
    background: var(--page);
  }
  .canvas {
    position: relative;
    width: 1200px;
    height: 911px;
  }
  .banner {
    position: absolute;
    top: 17px;
    width: 352px;
    height: 882px;
    overflow: hidden;
  }
  .banner--truth { left: 25px; }
  .banner--love { left: 434px; }
  .banner--mission { left: 823px; }

  .banner__texture {
    position: absolute;
    inset: 0;
    background: linear-gradient(180deg,
      var(--blue-mid) 0%,
      var(--blue-deep) 35%,
      var(--blue-deep) 62%,
      var(--blue-bright) 82%,
      var(--cyan-light) 100%);
  }
  .banner--love .banner__texture {
    background: linear-gradient(180deg,
      var(--cyan-light) 0%,
      var(--blue-bright) 16%,
      var(--blue-deep) 32%,
      var(--blue-deep) 70%,
      var(--blue-mid) 100%);
  }
  .banner__frame {
    position: absolute;
    left: 18px;
    top: 19px;
    right: 18px;
    bottom: 19px;
    border: 5px solid var(--white);
  }
  .banner__word {
    position: absolute;
    left: calc(50% + 10px);
    top: 50%;
    margin: 0;
    transform: translate(-50%, -50%) rotate(-90deg);
    font-family: "Bebas Neue", "Arial Narrow", sans-serif;
    font-weight: 400;
    font-size: 198px;
    line-height: 1;
    letter-spacing: 0.02em;
    color: var(--white);
    white-space: nowrap;
  }
  .brand {
    position: absolute;
    left: 48px;
    display: flex;
    align-items: center;
    gap: 10px;
    color: var(--white);
    font-family: "Montserrat", Arial, sans-serif;
    font-weight: 700;
  }
  .brand--top { top: 40px; }
  .brand--bottom { bottom: 58px; }
  .brand__mark {
    width: 48px;
    height: 48px;
    border: 3px solid var(--white);
    border-radius: 50%;
    box-sizing: border-box;
    flex: none;
  }
  .brand__name {
    display: flex;
    flex-direction: column;
    line-height: 1;
  }
  .brand__title {
    font-size: 20px;
    letter-spacing: 0.01em;
  }
  .brand__tagline {
    margin-top: 4px;
    font-size: 6px;
    letter-spacing: 0.3em;
  }
</style>
</head>
<body>
<main class="canvas">

  <section class="banner banner--truth">
    <div class="banner__texture" role="img" aria-label="Blue and cyan painted brushstroke texture"></div>
    <div class="banner__frame"></div>
    <div class="brand brand--top">
      <span class="brand__mark"></span>
      <span class="brand__name">
        <span class="brand__title">MEADOWBROOK</span>
        <span class="brand__tagline">FELLOWSHIP CHAPEL · RIVERSIDE</span>
      </span>
    </div>
    <h2 class="banner__word">TRUTH</h2>
  </section>

  <section class="banner banner--love">
    <div class="banner__texture" role="img" aria-label="Blue and cyan painted brushstroke texture"></div>
    <div class="banner__frame"></div>
    <h2 class="banner__word">LOVE</h2>
    <div class="brand brand--bottom">
      <span class="brand__mark"></span>
      <span class="brand__name">
        <span class="brand__title">MEADOWBROOK</span>
        <span class="brand__tagline">FELLOWSHIP CHAPEL · RIVERSIDE</span>
      </span>
    </div>
  </section>

  <section class="banner banner--mission">
    <div class="banner__texture" role="img" aria-label="Blue and cyan painted brushstroke texture"></div>
    <div class="banner__frame"></div>
    <div class="brand brand--top">
      <span class="brand__mark"></span>
      <span class="brand__name">
        <span class="brand__title">MEADOWBROOK</span>
        <span class="brand__tagline">FELLOWSHIP CHAPEL · RIVERSIDE</span>
      </span>
    </div>
    <h2 class="banner__word">MISSION</h2>
  </section>

</main>
</body>
</html>
```